Maple Harbor Home Care Business Cards

We are looking to create double sided, sleek business cards for our new Home Health Care Agency, Maple Harbor Home Care, located in NJ. We want to appear established, professional and at the same time, stand out with a creative and original flair. It should have a luxurious, exclusive feel to it.
The theme colors from our logo should be incorporated into the project.

Our Logo is attached.

Information to be included on the business cards:

Insert Phone Icon: (555)-403-2297
Insert Website Icon: mhhcxq.example
Insert E-mail Icon: info@mhhcxq.example

Follow us on Social Media!
Insert Facebook Icon: (I will provide the link at a later time)
Insert Instagram Icon (I will provide the link at a later time)

In regard to location, we service the areas of: Bayville
Beachwood
Brick
Deal
Howell
Island Heights
Jackson
Lakehurst
Lakewood
Manchester Township
Point Pleasant Beach
Roosevelt
Long Branch
Toms River

All all it's neighboring areas.

However, that can take up a lot of room...therefore, I had in mind to use the backside of the card to have a MAP with all these areas marked on there...in addition to listing these service locations below the map.

We want the card to appear lively and vibrant.

Please note: I will provide the potential winner with the contact's name later on in the process.

A sample idea is attached below as well.

Use your creative juices!

Good luck!

• A map of our service areas on the back of the double sided card.
Sleek design
Our logo (refer to attachment below)

```html
<!DOCTYPE html>
<html lang="en">
<head>
<meta charset="utf-8">
<title>Maple Harbor Home Care – Business Cards</title>
<link href="https://fonts.googleapis.com/css2?family=Montserrat:wght@700&family=Roboto:wght@400;500;700&display=swap" rel="stylesheet">
<style>
  :root {
    --bg: #d4d4d4;
    --navy: #15498f;
    --deep-blue: #0f4a8c;
    --teal: #1d6a78;
    --green: #7cc242;
    --leaf: #5fb346;
    --ink: #1b1b1b;
    --paper: #ffffff;
    --paper-tint: #f3f5f7;
    --faint: #e4e9ef;
  }
  * { box-sizing: border-box; margin: 0; padding: 0; }
  html, body { width: 1200px; height: 852px; overflow: hidden; }
  body {
    background: var(--bg);
    position: relative;
    font-family: "Roboto", Arial, sans-serif;
  }
  .card {
    position: absolute;
    width: 560px;
    height: 320px;
    border-radius: 22px;
    overflow: hidden;
    box-shadow: 0 10px 24px rgba(0,0,0,.25);
  }

  /* ---------- Back side ---------- */
  .card-back {
    left: 150px; top: 60px;
    background: linear-gradient(225deg, var(--green) 0%, var(--teal) 55%, var(--deep-blue) 100%);
    color: var(--paper);
  }
  .service-map {
    position: absolute;
    left: 90px; top: 30px;
    width: 420px; height: 190px;
    border-radius: 40px;
    background: radial-gradient(ellipse at center, rgba(20,70,90,.35) 0%, rgba(20,70,90,.12) 60%, rgba(20,70,90,0) 80%);
  }
  .back-brand {
    position: absolute;
    left: 0; right: 0; top: 72px;
    text-align: center;
  }
  .back-brand .mark {
    display: block;
    width: 46px; height: 46px;
    margin: 0 auto 12px;
    border-radius: 50%;
    border: 3px solid var(--paper);
  }
  .brand-name {
    font-family: "Montserrat", Arial, sans-serif;
    font-weight: 700;
    font-size: 24px;
    letter-spacing: .5px;
    text-transform: uppercase;
  }
  .back-brand .tagline {
    display: inline-block;
    margin-top: 6px;
    padding-top: 5px;
    border-top: 1.5px solid var(--paper);
    font-size: 11px;
    letter-spacing: 2.4px;
    text-transform: uppercase;
    font-weight: 500;
  }
  .service-areas {
    position: absolute;
    left: 30px; right: 30px; bottom: 30px;
    text-align: center;
    font-size: 14.5px;
    line-height: 1.6;
  }
  .service-areas .sep { opacity: .8; padding: 0 5px; }

  /* ---------- Front side ---------- */
  .card-front {
    left: 490px; top: 440px;
    background: linear-gradient(135deg, var(--paper) 55%, var(--paper-tint) 100%);
  }
  .front-glow {
    position: absolute;
    right: -60px; top: -70px;
    width: 300px; height: 300px;
    border-radius: 50%;
    border: 28px solid var(--faint);
    opacity: .7;
  }
  .front-brand {
    position: absolute;
    left: 34px; top: 74px;
    display: flex; align-items: center; gap: 14px;
  }
  .front-brand .mark {
    width: 64px; height: 64px;
    border-radius: 50%;
    border: 5px solid var(--green);
    flex: none;
  }
  .front-brand .brand-name { color: var(--navy); font-size: 23px; line-height: 1.05; }
  .front-brand .tagline {
    margin-top: 6px;
    padding-top: 4px;
    border-top: 1.5px solid var(--green);
    color: var(--navy);
    font-size: 10px;
    letter-spacing: 2px;
    font-weight: 500;
    text-transform: uppercase;
  }
  .holder {
    position: absolute;
    left: 36px; top: 212px;
  }
  .holder-name {
    font-size: 19px; font-weight: 700; color: var(--navy);
  }
  .holder-name .last { color: var(--leaf); }
  .holder-role { margin-top: 5px; font-size: 14px; color: var(--ink); }
  .contact {
    position: absolute;
    left: 350px; top: 164px;
    list-style: none;
    font-size: 14px;
    color: var(--ink);
  }
  .contact li { display: flex; align-items: center; gap: 9px; height: 20px; }
  .contact svg { width: 13px; height: 13px; fill: var(--navy); flex: none; }
  .front-bands { position: absolute; inset: 0; width: 560px; height: 320px; }
  .social {
    position: absolute;
    right: 26px; top: 276px;
    display: flex; align-items: center; gap: 8px;
    color: var(--paper); font-size: 14px;
    white-space: nowrap;
  }
  .social .dot { width: 12px; height: 12px; border-radius: 50%; background: var(--paper); }
</style>
</head>
<body>

<section class="card card-back" aria-label="Card back">
  <div class="service-map" role="img" aria-label="Faint map of the service region"></div>
  <div class="back-brand">
    <span class="mark"></span>
    <div class="brand-name">Maple Harbor Home Care</div>
    <div class="tagline">Caring close to home every day</div>
  </div>
  <p class="service-areas">
    Cedarton<span class="sep">|</span>Birchmoor<span class="sep">|</span>Stone<span class="sep">|</span>Vale<span class="sep">|</span>Hollis<span class="sep">|</span>Harbor Heights<br>
    Ashford<span class="sep">|</span>Lakemont<span class="sep">|</span>Ridgewell<span class="sep">|</span>Millbrook Township<br>
    Port Haven Beach<span class="sep">|</span>Kingsley<span class="sep">|</span>Long Cove<span class="sep">|</span>Elm River
  </p>
</section>

<section class="card card-front" aria-label="Card front">
  <div class="front-glow"></div>
  <svg class="front-bands" viewBox="0 0 560 320" aria-hidden="true">
    <polygon points="0,302 368,272 356,298 0,320" fill="var(--green)"/>
    <path d="M352,320 L368,280 Q374,266 390,264 L560,238 L560,320 Z" fill="var(--navy)"/>
  </svg>

  <div class="front-brand">
    <span class="mark"></span>
    <div>
      <div class="brand-name">Maple Harbor<br>Home Care</div>
      <div class="tagline">Caring close to home every day</div>
    </div>
  </div>

  <div class="holder">
    <div class="holder-name">Jordan Ellis <span class="last">Reed</span></div>
    <div class="holder-role">Managing Director</div>
  </div>

  <ul class="contact">
    <li>
      <svg viewBox="0 0 24 24"><path d="M6.6 10.8a15 15 0 0 0 6.6 6.6l2.2-2.2c.3-.3.7-.4 1-.2 1.1.4 2.3.6 3.6.6.6 0 1 .4 1 1V20c0 .6-.4 1-1 1A17 17 0 0 1 3 4c0-.6.4-1 1-1h3.5c.6 0 1 .4 1 1 0 1.3.2 2.5.6 3.6.1.3 0 .7-.2 1z"/></svg>
      (555)-403-2297
    </li>
    <li>
      <svg viewBox="0 0 24 24"><path d="M2 5h20v14H2z M3.5 6.5 12 13l8.5-6.5" stroke="#fff" stroke-width="1.5"/></svg>
      info@mhhcxq.example
    </li>
    <li>
      <svg viewBox="0 0 24 24"><circle cx="12" cy="12" r="10"/><path d="M2 12h20M12 2c3 3 3 17 0 20M12 2c-3 3-3 17 0 20" stroke="#fff" stroke-width="1.3" fill="none"/></svg>
      mhhcxq.example
    </li>
  </ul>

  <div class="social">
    <span class="dot"></span>
    @mapleharborcare
  </div>
</section>

</body>
</html>
```